ebook Template (Word or PowerPoint format)

I would like a template for creating ebooks. The end product must be in Word or PowerPoint so that I can edit it. It should be consistently branded, based on the look and feel of the website http://www.brl.ns.ca/home . It should make strong use of visual... we have tons of great photos. It could be used for Games At Marlow Brookfield -- showcasing our sports. Or travel with Marlow Brookfield. There should be an intro page that will be a bit text heavy and closing page with ample room for text as well. The interior should have a few different layouts to choose from with varying image and text block sizes.

Target Market(s)

Parents of prospective student at a private school

Industry/Entity Type

Product

Font styles to use
Serif
Sans Serif

Requirements
Must have
• Be in WORD or POWERPOINT.
Nice to have
• a few interior page options
• branding throughout.
• a strong cover and call to action page with company info (found on the website)

```html
<!DOCTYPE html>
<html lang="en">
<head>
<meta charset="utf-8">
<title>Marlow Brookfield School — Intro Page</title>
<link rel="stylesheet" href="https://fonts.googleapis.com/css2?family=Libre+Franklin:wght@500;600&family=Tinos:wght@400;700&display=swap">
<style>
  :root {
    --brand-red: #a4002d;
    --headline-red: #8a0f0f;
    --frame-red: #8c0c0c;
    --frame-grey: #e2e2e2;
    --ink: #111111;
    --paper: #ffffff;
    --folio: #3b3530;
    --leaf-orange: #d9862a;
    --leaf-gold: #e7b25a;
    --leaf-rust: #b4521e;
  }
  * { box-sizing: border-box; margin: 0; padding: 0; }
  html, body { width: 841px; height: 1200px; overflow: hidden; background: var(--paper); }
  .page {
    position: relative; width: 841px; height: 1200px; overflow: hidden;
    background: var(--paper); color: var(--ink);
    font-family: "Tinos", "Times New Roman", serif;
  }
  .foliage-top {
    position: absolute; left: 0; top: 0; width: 841px; height: 200px;
    background:
      radial-gradient(ellipse at 12% 25%, var(--leaf-rust) 0%, transparent 45%),
      radial-gradient(ellipse at 85% 20%, var(--leaf-gold) 0%, transparent 50%),
      linear-gradient(180deg, var(--leaf-orange) 0%, var(--leaf-gold) 55%, rgba(255,255,255,0) 100%);
  }
  .foliage-bottom {
    position: absolute; left: 0; bottom: 0; width: 841px; height: 115px;
    background:
      radial-gradient(ellipse at 20% 90%, var(--leaf-rust) 0%, transparent 50%),
      radial-gradient(ellipse at 80% 85%, var(--leaf-rust) 0%, transparent 45%),
      linear-gradient(0deg, var(--leaf-orange) 0%, var(--leaf-gold) 50%, rgba(255,255,255,0) 100%);
  }
  .brand-tab { position: absolute; left: 249px; top: 0; width: 350px; height: 216px; }
  .brand-tab svg { position: absolute; inset: 0; }
  .brand-name {
    position: absolute; left: 0; right: 0; top: 96px; text-align: center;
    color: var(--paper); font-family: "Tinos", "Times New Roman", serif;
    font-size: 27px; font-weight: 400;
  }
  .brand-mark {
    position: absolute; left: 157px; top: 42px; width: 36px; height: 36px;
    border-radius: 50%; background: rgba(255,255,255,0.85);
  }
  .headline {
    position: absolute; left: 69px; top: 236px;
    font-family: "Libre Franklin", "Franklin Gothic Medium", sans-serif;
    font-weight: 500; font-size: 45px; letter-spacing: -0.3px;
    color: var(--headline-red); line-height: 1;
  }
  .intro-copy { position: absolute; left: 69px; top: 305px; width: 703px; }
  .lead-photo {
    float: right; width: 350px; height: 238px; margin: 8px -29px 10px 18px;
    background: var(--frame-grey); border-radius: 4px; padding: 10px 9px 9px;
  }
  .photo-fill { width: 100%; height: 100%; }
  .lead-photo .photo-fill { background: linear-gradient(180deg, #d9cfbd 0%, #a99a85 55%, #4e4a47 100%); }
  .standfirst { font-weight: 700; font-size: 15.4px; line-height: 19px; margin-bottom: 17px; }
  .body-text { font-size: 13.6px; line-height: 15.7px; margin-bottom: 16px; }
  .feature-photo {
    position: absolute; left: 57px; top: 816px; width: 352px; height: 306px;
    background: var(--frame-grey); border-radius: 4px; padding: 10px 9px 9px;
  }
  .feature-photo .photo-fill { background: linear-gradient(180deg, #7fa2cf 0%, #c9b98a 35%, #e3cf3a 65%, #5b7b3c 100%); }
  .contents {
    position: absolute; left: 428px; top: 821px; width: 376px; height: 296px;
    border: 9px solid var(--frame-red); border-radius: 4px; background: var(--paper);
    padding: 12px 18px 0 10px;
    box-shadow: 0 2px 4px rgba(0,0,0,0.35);
  }
  .contents-title {
    font-family: "Libre Franklin", "Franklin Gothic Medium", sans-serif;
    font-weight: 500; font-size: 42px; color: var(--headline-red); line-height: 1;
    margin-bottom: 16px;
  }
  .contents-list { list-style: none; }
  .contents-item {
    display: flex; align-items: baseline; font-weight: 700; font-size: 15.5px;
    height: 36px; line-height: 36px;
  }
  .contents-leader { flex: 1; border-bottom: 2px dotted var(--ink); margin: 0 2px; transform: translateY(-4px); }
  .folio {
    position: absolute; left: 393px; top: 1140px; width: 49px; height: 32px;
    background: var(--folio); color: var(--paper);
    font-family: "Libre Franklin", sans-serif; font-weight: 600; font-size: 14px;
    text-align: center; line-height: 30px;
  }
</style>
</head>
<body>
<main class="page">
  <div class="foliage-top" role="img" aria-label="Autumn maple leaves in orange and gold"></div>
  <div class="foliage-bottom" role="img" aria-label="Autumn maple leaves in orange and gold"></div>

  <header class="brand-tab">
    <svg width="350" height="216" viewBox="0 0 350 216" aria-hidden="true">
      <polygon points="4,0 346,0 346,190 0,214" fill="#8c0c0c" opacity="0.35" transform="translate(2,3)"/>
      <polygon points="0,0 346,0 346,190 0,212" fill="var(--brand-red)"/>
    </svg>
    <span class="brand-mark" aria-hidden="true"></span>
    <div class="brand-name">Marlow Brookfield School</div>
  </header>

  <h1 class="headline">Intro page headline goes here.</h1>

  <section class="intro-copy">
    <figure class="lead-photo"><div class="photo-fill" role="img" aria-label="Three staff members presenting an award plaque in a dining hall"></div></figure>
    <p class="standfirst">Lupti nus as poribernam acerchilitat vitatur reptas asinum rereicat audanih iligendae ne es cones mos que volorro qui occum dolupta ecaborro molest pe num sam erum a dolupti ut experias et labo. Nequi utem antur? Odipsam usdanda inctibusae cum alitati cum harum dolesti nctatur eperum aut molluptas que que inimpora id quat as issi re nestius con re sita vendunt que nam quos molupturio cusdant.</p>
    <p class="body-text">Soluptates accae. Et fugiatis alignatempe labo. Sed et atis eatquis derum re iumqui omnimus exerro od etur?</p>
    <p class="body-text">Ducid quam hiciis maior ad ut optatiisti sero molupicia cum ad mos dolorepro temporiore nis earuptatur anda intio dolore, explignihit reptatem aci conseque esti am dis quos pernati to quo blaborum essi dis es evel inciae volore dolo volest, velis necus erum qui dolendi doluptiis utatione voluptat eatiundit, tet iunt accum esequi inversp ediant es audae nestion et, nis aut licatatatem. Illecabori cullam numenitaque eium ea porepra is et es dunt, quia velici di bereicient qui sequidigni sime comnihilles nulparum, que molorestrum ab int aut incia sin nonsecea velit omnimuscidis repuditatque quid ma voluptus, con ne niet faccuptis acia consento eatiusae vendant voluptibusam reria num inulpa veleste mporepe rferis qui dolupta nim de volorpo rporro quiandant que moluptatiam quis moditiis estinum si te et earum sam core, corumendant volupta sperio te voluptas ipicitae parum quibeati ut quis iurestrum quae parum qui nis voluptat quid quam fuga. Udi accus inulpa volenis eratur molorepe volumque endemped mo quae sitiam vent quo int auda perspid enditecto te doluptur? Qui blaut lame et eossum remodi dolupta quas apitibu stiore optur mi, conesequost ped quam nisqui ommo erspis ersped quasped maion raturero test hit, te officia discim quibust iaessi re ratum ut ex eatem aut offic to comnisi nverior alicil iur, quatem fugia plaboreprо ommodit pelestium quiate comnihi ligendanti temquid mi, sequidigni sime comnihilles nulparum, que molorestrum ab int aut incia sin nonsecea velit omnimuscidis repuditatque quid ma voluptus, con ne niet faccuptis acia consento eatiusae vendant voluptibusam reria num inulpa veleste mporepe rferis qui dolupta nim de volorpo rporro quiandant que moluptatiam quis moditiis estinum si te et earum sam core,</p>
  </section>

  <figure class="feature-photo"><div class="photo-fill" role="img" aria-label="Students in yellow costumes gathered outdoors at a school sports event"></div></figure>

  <nav class="contents" aria-label="Contents">
    <h2 class="contents-title">Contents.</h2>
    <ul class="contents-list">
      <li class="contents-item"><span>Article</span><span class="contents-leader"></span><span>PG#</span></li>
      <li class="contents-item"><span>Article</span><span class="contents-leader"></span><span>PG#</span></li>
      <li class="contents-item"><span>Article</span><span class="contents-leader"></span><span>PG#</span></li>
      <li class="contents-item"><span>Article</span><span class="contents-leader"></span><span>PG#</span></li>
      <li class="contents-item"><span>Article</span><span class="contents-leader"></span><span>PG#</span></li>
      <li class="contents-item"><span>Article</span><span class="contents-leader"></span><span>PG#</span></li>
    </ul>
  </nav>

  <div class="folio">2</div>
</main>
</body>
</html>
```